New Web Site Design - Ironwood Signal Solutions

We are looking for a completely new web site design. Ironwood Signal Solutions is a full service company providing PBX and IP/Cloud Based phone systems. We also sell and install video camera surveillance systems and provide low voltage cabling services (CAT5 and CAT3). We are looking for something professional looking. We want to be able to showcase our vendor partners as well as be able to show photos of some of the work we have done. We will also want to be able to post PDF brochures as well as make changes to the website ourselves.

Target Market(s)

Commercial

Industry/Entity Type

Communication

Coding

Coded - Design and coding required

Number of Pages Required

5+ page

Font styles to use
Sans Serif

Colors
0455a3

Requirements
Must have
• Ability to upload PDF brochures
• Professional look and feel
• Ability to upload and easily insert job photos
• Thinking it should have at least 6 pages: Main page, phone systems and services page, carrier services page, video surveillance systems and service page, low voltage cabling services page, contact us page

```html
<!DOCTYPE html>
<html lang="en">
<head>
<meta charset="utf-8">
<title>Ironwood Signal Solutions</title>
<link rel="stylesheet" href="https://fonts.googleapis.com/css2?family=Roboto:wght@400;500;700&family=Roboto+Condensed:wght@500;700&display=swap">
<style>
:root{
  --navy:#0c2b66;
  --brand:#0455a3;
  --gold:#f3b20f;
  --ink:#1c1c1c;
  --muted:#6d6d6d;
  --line:#dedede;
  --white:#ffffff;
  --dark:#2b2b2b;
}
*{box-sizing:border-box;margin:0;padding:0}
html,body{width:1200px;height:3429px;overflow:hidden;background:var(--white)}
body{position:relative;font-family:"Roboto",Arial,sans-serif;color:var(--ink)}
.abs{position:absolute}

/* header */
.site-header{position:absolute;left:0;top:0;width:1200px;height:78px;background:var(--white);box-shadow:0 1px 4px rgba(0,0,0,.08);z-index:5}
.menu-toggle{left:100px;top:28px}
.brand{left:152px;top:22px}
.brand-name{display:block;font-size:17px;font-weight:500;color:var(--navy);line-height:1.1;width:170px}
.main-nav{left:516px;top:0;display:flex;height:78px}
.main-nav a{display:flex;align-items:center;padding:0 13px;font-size:13px;font-weight:500;color:var(--ink);text-decoration:none}
.main-nav a.active{background:var(--navy);color:var(--white)}
.search-btn{left:1058px;top:20px;width:38px;height:38px;border-radius:50%;background:var(--brand);display:flex;align-items:center;justify-content:center}
.account-menu{left:98px;top:78px;width:229px;background:var(--navy);z-index:6}
.account-menu a{display:block;color:var(--white);font-size:12px;padding:12px 30px;text-decoration:none}
.account-menu a+a{border-top:1px solid rgba(255,255,255,.2)}

/* hero */
.hero{left:0;top:78px;width:1200px;height:477px;background:linear-gradient(90deg,#f4f5f7 0%,#e9ecef 40%,#c9ccd1 60%,#a7a9ad 100%)}
.hero h1{left:201px;top:126px;font-size:40px;font-weight:500;line-height:1.18;color:#111}
.hero p{left:201px;top:244px;width:360px;font-size:12px;line-height:1.55;color:#222}
.btn{display:inline-flex;align-items:center;justify-content:center;font-size:12px;font-weight:500;text-decoration:none;text-transform:uppercase}
.btn-solid{background:var(--navy);color:var(--white)}
.btn-outline{border:2px solid var(--navy);color:var(--navy);background:var(--white)}
.hero .btn-solid{left:201px;top:331px;width:158px;height:46px;position:absolute}
.hero .btn-outline{left:375px;top:331px;width:192px;height:46px;position:absolute}
.hero-arrow{top:228px}

/* feature strip */
.feature{position:absolute;top:601px;width:320px;display:flex;gap:14px}
.feature .thumb{width:108px;height:92px;flex:none;background:linear-gradient(135deg,#6f8dab,#33475e)}
.feature h3,.news-item h3{font-size:13px;font-weight:500;color:#222;margin-bottom:6px}
.feature p,.news-item p{font-size:11px;line-height:1.4;color:var(--muted)}

/* video + news */
.video{left:98px;top:731px;width:661px;height:270px;background:linear-gradient(135deg,#7c8794,#4b5560 60%,#3a4048)}
.play{left:400px;top:847px;width:56px;height:40px;background:var(--white);border-radius:6px}
.play-label{left:370px;top:896px;font-size:10px;font-weight:700;color:var(--white)}
.news-title{left:784px;top:724px;font-size:29px;font-weight:500;color:#333;font-family:"Roboto Condensed",Arial,sans-serif}
.news-title span{color:var(--navy)}
.news-item{position:absolute;left:784px;width:316px;display:flex;gap:14px}
.news-item .thumb{width:108px;height:92px;flex:none;background:linear-gradient(135deg,#667383,#2d3640)}
.welcome h2{left:98px;top:1030px;font-family:"Roboto Condensed",Arial,sans-serif;font-size:30px;font-weight:500;color:#111}
.welcome h4{left:98px;top:1073px;font-size:16px;font-weight:400;color:var(--brand)}
.welcome p{left:98px;top:1120px;width:650px;font-size:11px;line-height:1.6;color:var(--muted)}
.welcome .btn{position:absolute;left:98px;top:1225px;width:119px;height:35px}

/* services */
.services{left:0;top:1301px;width:1200px;height:363px;background:linear-gradient(180deg,#2c2c2c,#3c3c3c 60%,#2a2a2a)}
.section-title{position:absolute;left:0;width:1200px;text-align:center;font-size:25px;font-weight:500}
.section-lead{position:absolute;left:210px;width:780px;text-align:center;font-size:13px;font-style:italic;line-height:1.6}
.service{position:absolute;top:1479px;width:240px;text-align:center}
.service .icon{width:99px;height:99px;margin:0 auto;border:4px solid var(--gold);border-radius:8px;display:flex;align-items:center;justify-content:center}
.service h3{margin-top:30px;font-size:14px;font-weight:700;color:var(--white)}

/* carousel */
.work{position:absolute;top:1744px;width:229px}
.work .thumb{height:158px;background:linear-gradient(135deg,#9aa5b0,#46505b)}
.work h3{margin-top:26px;font-size:14px;font-weight:500;line-height:1.4;color:#111}
.work .bar{margin-top:16px;height:6px;display:flex}
.work .bar i{flex:1;background:var(--gold)}
.work .bar b{flex:2;background:var(--navy)}
.dots{left:576px;top:2043px;display:flex;gap:8px}
.dots i{width:9px;height:9px;border-radius:50%;background:#555}
.dots i.on{background:var(--gold)}
.divider{left:98px;top:2089px;width:1003px;height:1px;background:var(--line)}

/* included */
.included-panel{left:0;top:2124px;width:331px;height:281px;background:var(--navy)}
.included-panel h2{position:absolute;right:30px;bottom:28px;text-align:right;font-family:"Roboto Condensed",Arial,sans-serif;font-size:40px;font-weight:700;line-height:1;color:var(--gold)}
.included-photo{left:331px;top:2124px;width:343px;height:281px;background:linear-gradient(135deg,#1c2c4a,#4a6c8f 50%,#c9ccd0)}
.checklist{left:702px;top:2143px;list-style:none}
.checklist li{height:31px;display:flex;align-items:center;gap:14px;font-size:11px;color:#444}

/* blog */
.blog-card{position:absolute;top:2615px;width:318px;height:418px;border:1px solid var(--line);padding:22px 22px}
.blog-card .thumb{height:178px;background:linear-gradient(135deg,#d4d8dd,#7d8794)}
.blog-card h3{margin-top:34px;font-size:17px;font-weight:500;color:#222}
.blog-card h5{margin-top:6px;font-size:10px;font-weight:400;color:var(--muted);padding-bottom:12px;border-bottom:1px solid var(--line)}
.blog-card p{margin-top:12px;font-size:11px;line-height:1.55;color:var(--muted)}
.blog-card .btn{margin-top:14px;width:110px;height:38px}

/* footer */
.site-footer{left:0;top:3070px;width:1200px;height:359px;background:var(--navy);color:var(--white)}
.footer-col{position:absolute;top:42px;font-size:12px;line-height:1.6}
.footer-col h4{font-size:19px;font-weight:500;margin-bottom:18px}
.footer-brand{display:block;font-size:15px;font-weight:500;line-height:1.2;margin-bottom:14px;color:var(--white)}
.footer-col .meta{opacity:.85;margin-bottom:14px}
.signup{display:flex;margin-top:20px;width:230px;height:38px;background:var(--white);border-radius:19px}
.signup b{margin-left:auto;width:52px;background:var(--gold);border-radius:19px;display:flex;align-items:center;justify-content:center;font-size:12px;font-weight:700}
.gallery{display:grid;grid-template-columns:repeat(3,60px);gap:22px 24px}
.gallery i{height:56px;background:linear-gradient(135deg,#e6e9ee,#8a95a3)}
</style>
</head>
<body>

<header class="site-header">
  <svg class="abs menu-toggle" width="28" height="22" viewBox="0 0 28 22"><path d="M0 2h28M0 11h28M0 20h28" stroke="#222" stroke-width="3"/></svg>
  <div class="abs brand"><span class="brand-name">Ironwood Signal Solutions</span></div>
  <nav class="abs main-nav">
    <a class="active" href="#">Home</a><a href="#">About Us</a><a href="#">Services</a><a href="#">Products</a><a href="#">Projects</a><a href="#">Blog</a><a href="#">Contact Us</a>
  </nav>
  <div class="abs search-btn"><svg width="16" height="16" viewBox="0 0 16 16"><circle cx="6.5" cy="6.5" r="5" fill="none" stroke="#fff" stroke-width="2"/><path d="M10 10l5 5" stroke="#fff" stroke-width="2"/></svg></div>
</header>
<div class="abs account-menu"><a href="#">Sign In</a><a href="#">Create a SignalHub Account</a></div>

<section class="abs hero" role="img" aria-label="Photo of two colleagues working together at a laptop in a bright office">
  <h1 class="abs">Contrary To<br>Popular Belief</h1>
  <p class="abs">Contrary to popular belief, Lorem Ipsum is not simply random text. It has roots in a piece of classical Latin literature from 45 BC, making it over 2000 years old.</p>
  <a class="btn btn-solid" href="#">Explore</a>
  <a class="btn btn-outline" href="#">Download Brochure</a>
  <svg class="abs hero-arrow" style="left:100px" width="24" height="20" viewBox="0 0 24 20"><path d="M22 10H3M10 2L2 10l8 8" fill="none" stroke="#111" stroke-width="2.5"/></svg>
  <svg class="abs hero-arrow" style="left:1076px" width="24" height="20" viewBox="0 0 24 20"><path d="M2 10h19M14 2l8 8-8 8" fill="none" stroke="#fff" stroke-width="2.5"/></svg>
</section>

<div class="feature" style="left:98px"><span class="thumb" role="img" aria-label="Photo of a technician on the phone"></span><div><h3>LOREM IPSUM DUMMY</h3><p>Contrary to popular belief, Lorem Ipsum is not simply random text. It has roots in a piece of classical</p></div></div>
<div class="feature" style="left:439px"><span class="thumb" role="img" aria-label="Photo of a monitoring desk"></span><div><h3>LOREM IPSUM DUMMY</h3><p>Contrary to popular belief, Lorem Ipsum is not simply random text. It has roots in a piece of classical</p></div></div>
<div class="feature" style="left:782px"><span class="thumb" role="img" aria-label="Photo of a technician on the phone"></span><div><h3>LOREM IPSUM DUMMY</h3><p>Contrary to popular belief, Lorem Ipsum is not simply random text. It has roots in a piece of classical</p></div></div>

<div class="abs video" role="img" aria-label="Video still of hands typing on a laptop"></div>
<div class="abs play"><svg width="56" height="40" viewBox="0 0 56 40"><path d="M22 11l14 9-14 9z" fill="#333"/></svg></div>
<div class="abs play-label">CLICK HERE TO PLAY</div>

<h2 class="abs news-title">NEWS &amp; <span>EVENTS</span></h2>
<div class="news-item" style="top:784px"><span class="thumb" role="img" aria-label="Event photo"></span><div><h3>LOREM IPSUM DUMMY</h3><p>Contrary to popular belief, Lorem Ipsum is not simply random text. It has roots in a piece of classical</p></div></div>
<div class="news-item" style="top:912px"><span class="thumb" role="img" aria-label="Event photo"></span><div><h3>LOREM IPSUM DUMMY</h3><p>Contrary to popular belief, Lorem Ipsum is not simply random text. It has roots in a piece of classical</p></div></div>
<div class="news-item" style="top:1042px"><span class="thumb" role="img" aria-label="Event photo"></span><div><h3>LOREM IPSUM DUMMY</h3><p>Contrary to popular belief, Lorem Ipsum is not simply random text. It has roots in a piece of classical</p></div></div>
<div class="news-item" style="top:1170px"><span class="thumb" role="img" aria-label="Event photo"></span><div><h3>LOREM IPSUM DUMMY</h3><p>Contrary to popular belief, Lorem Ipsum is not simply random text. It has roots in a piece of classical</p></div></div>

<div class="welcome">
  <h2 class="abs">WELCOME TO IRONWOOD SIGNAL SOLUTIONS</h2>
  <h4 class="abs">LOREM IPSUM DUMMY TEXT</h4>
  <p class="abs">Contrary to popular belief, Lorem Ipsum is not simply random text. It has roots in a piece of classical Latin literature from 45 BC, making it over 2000 years old. A Latin professor in Virginia looked up one of the more obscure Latin words, consectetur, from a Lorem Ipsum passage, and going through the cites of the word in classical literature, discovered the undoubtable source.</p>
  <a class="btn btn-solid" href="#">Explore</a>
</div>

<section class="abs services" role="img" aria-label="Dark photo of a team at a meeting table">
  <h2 class="section-title" style="top:44px;color:#fff">Our Services</h2>
  <p class="section-lead" style="top:88px;color:#eee">Lorem Ipsum is simply dummy text of the printing and typesetting industry. Lorem Ipsum has been the industry's standard dummy text ever since the 1500s, when an unknown printer took a galley of type and scrambled it to make a</p>
</section>
<div class="service" style="left:102px"><div class="icon"><svg width="56" height="56" viewBox="0 0 56 56" fill="none" stroke="#fff" stroke-width="2.5"><rect x="10" y="8" width="36" height="24"/><path d="M28 32v8M14 48l6-8h16l6 8M20 14h16M20 20h10"/></svg></div><h3>LOREM IPSUM DUMMY</h3></div>
<div class="service" style="left:353px"><div class="icon"><svg width="56" height="56" viewBox="0 0 56 56" fill="none" stroke="#fff" stroke-width="2.5"><rect x="12" y="10" width="32" height="38"/><path d="M19 24h18M19 31h18M19 38h12M22 6l6 8 6-8"/></svg></div><h3>LOREM IPSUM DUMMY</h3></div>
<div class="service" style="left:605px"><div class="icon"><svg width="56" height="56" viewBox="0 0 56 56" fill="none" stroke="#fff" stroke-width="2.5"><rect x="10" y="8" width="36" height="24"/><path d="M28 32v8M14 48l6-8h16l6 8M20 14h16M20 20h10"/></svg></div><h3>LOREM IPSUM DUMMY</h3></div>
<div class="service" style="left:858px"><div class="icon"><svg width="56" height="56" viewBox="0 0 56 56" fill="none" stroke="#fff" stroke-width="2.5"><rect x="12" y="10" width="32" height="38"/><path d="M19 24h18M19 31h18M19 38h12M22 6l6 8 6-8"/></svg></div><h3>LOREM IPSUM DUMMY</h3></div>

<div class="work" style="left:98px"><div class="thumb" role="img" aria-label="Photo of a security operator at monitors"></div><h3>Lorem Ipsum Is Simply A<br>Dummy Text</h3><div class="bar"><i></i><b></b></div></div>
<div class="work" style="left:357px"><div class="thumb" role="img" aria-label="Photo of a hand lifting a desk phone"></div><h3>Lorem Ipsum Is Simply A<br>Dummy Text</h3><div class="bar"><i></i><b></b></div></div>
<div class="work" style="left:613px"><div class="thumb" role="img" aria-label="Photo of a control room desk with screens"></div><h3>Lorem Ipsum Is Simply A<br>Dummy Text</h3><div class="bar"><i></i><b></b></div></div>
<div class="work" style="left:871px"><div class="thumb" role="img" aria-label="Photo of a network recorder unit"></div><h3>Lorem Ipsum Is Simply A<br>Dummy Text</h3><div class="bar"><i></i><b></b></div></div>
<div class="abs dots"><i></i><i class="on"></i><i></i></div>
<div class="abs divider"></div>

<div class="abs included-panel"><h2>WHAT'S<br>INCLUDED</h2></div>
<div class="abs included-photo" role="img" aria-label="Photo of a technician working at a cabling rack"></div>
<ul class="abs checklist">
  <li><svg width="12" height="10" viewBox="0 0 12 10"><path d="M1 5l3.5 3.5L11 1" fill="none" stroke="#f3b20f" stroke-width="2"/></svg>Contrary to popular belief, Lorem Ipsum is not simply random text.</li>
  <li><svg width="12" height="10" viewBox="0 0 12 10"><path d="M1 5l3.5 3.5L11 1" fill="none" stroke="#f3b20f" stroke-width="2"/></svg>Looked up one of the more obscure Latin words, consectetur.</li>
  <li><svg width="12" height="10" viewBox="0 0 12 10"><path d="M1 5l3.5 3.5L11 1" fill="none" stroke="#f3b20f" stroke-width="2"/></svg>Lorem Ipsum comes from sections 1.10.32.</li>
  <li><svg width="12" height="10" viewBox="0 0 12 10"><path d="M1 5l3.5 3.5L11 1" fill="none" stroke="#f3b20f" stroke-width="2"/></svg>Contrary to popular belief.</li>
  <li><svg width="12" height="10" viewBox="0 0 12 10"><path d="M1 5l3.5 3.5L11 1" fill="none" stroke="#f3b20f" stroke-width="2"/></svg>Lorem Ipsum comes from sections 1.10.32.</li>
  <li><svg width="12" height="10" viewBox="0 0 12 10"><path d="M1 5l3.5 3.5L11 1" fill="none" stroke="#f3b20f" stroke-width="2"/></svg>Contrary to popular belief, Lorem Ipsum is not simply random text.</li>
  <li><svg width="12" height="10" viewBox="0 0 12 10"><path d="M1 5l3.5 3.5L11 1" fill="none" stroke="#f3b20f" stroke-width="2"/></svg>Looked up one of the more obscure Latin words, consectetur.</li>
  <li><svg width="12" height="10" viewBox="0 0 12 10"><path d="M1 5l3.5 3.5L11 1" fill="none" stroke="#f3b20f" stroke-width="2"/></svg>Lorem Ipsum comes from sections 1.10.32.</li>
</ul>

<h2 class="section-title" style="top:2497px;color:#222">Latest From The Blog</h2>
<p class="section-lead" style="top:2545px;color:#666">Lorem Ipsum is simply dummy text of the printing and typesetting industry. Lorem Ipsum has been the industry's standard dummy text ever since the 1500s, when an unknown printer took a galley of type and scrambled it to make a</p>

<article class="blog-card" style="left:98px"><div class="thumb" role="img" aria-label="Photo of a hand writing on printed charts"></div><h3>LOREM IPSUM DUMMY</h3><h5>USED FOR TYPESETTING</h5><p>At vero eos et accusamus et iusto odio dignissi mos ducimus qui</p><a class="btn btn-outline" href="#">Read More</a></article>
<article class="blog-card" style="left:441px"><div class="thumb" role="img" aria-label="Photo of a business team in a meeting room"></div><h3>LOREM IPSUM DUMMY</h3><h5>USED FOR TYPESETTING</h5><p>At vero eos et accusamus et iusto odio dignissi mos ducimus qui</p><a class="btn btn-solid" href="#">Read More</a></article>
<article class="blog-card" style="left:782px"><div class="thumb" role="img" aria-label="Photo of colleagues around a laptop"></div><h3>LOREM IPSUM DUMMY</h3><h5>USED FOR TYPESETTING</h5><p>At vero eos et accusamus et iusto odio dignissi mos ducimus qui</p><a class="btn btn-outline" href="#">Read More</a></article>

<footer class="abs site-footer">
  <div class="footer-col" style="left:98px;width:220px">
    <span class="footer-brand">Ironwood Signal Solutions</span>
    <p class="meta">Maecenas etos sit amet, consectetur adipiscing elit. Terminal volutpat rutrum metro amet sollicitudin interdum.</p>
    <p>Phone: +1 (800) 555 0142<br>Address: 48 Harbor Line Avenue, New York<br>Email: hello@ironwoodsignal.test</p>
  </div>
  <div class="footer-col" style="left:354px;width:230px">
    <h4>Recent Posts</h4>
    <p class="meta">Sed laoreet sagittis molestie. Class aptent taciti sociosqu ad litora torquent per conubia nostra, p...</p>
    <p class="meta" style="margin-top:-8px">July 27, 2015 / 0 comments</p>
    <p class="meta">Aliquam et venenatis ante. Ut feugiat metus ante, nec lobortis arcu pulvinar sed. Nullam vehicula ma...</p>
    <p class="meta" style="margin-top:-8px">July 27, 2015 / 0 comments</p>
  </div>
  <div class="footer-col" style="left:613px;width:240px">
    <h4>Newsletter Signup</h4>
    <p class="meta">Temporibus autem quibusdam et aut officiis debitis aut rerum necessitatibus saepe eveniet ut et voluptates repudian.</p>
    <div class="signup"><b>GO</b></div>
  </div>
  <div class="footer-col" style="left:869px;width:240px">
    <h4>Gallery</h4>
    <div class="gallery" role="img" aria-label="Gallery of six small project photos"><i></i><i></i><i></i><i></i><i></i><i></i></div>
  </div>
</footer>

</body>
</html>
```